valtor clinic
cards
Professional
Martin Valtor D.C. D.A.B.C.O.
Chiroptactic Orthopedist
28615 Birchmont
Lakeview, OH 44990
kpm@valtorchiro.example
www.valtorchiro.example
M T W Th F S
Your Next Appointment Time

```html
<!DOCTYPE html>
<html lang="en">
<head>
<meta charset="utf-8">
<title>Valtor Clinic – Cards</title>
<link rel="stylesheet" href="https://fonts.googleapis.com/css2?family=Open+Sans:ital,wght@0,400;0,600;0,700;1,400&family=Cormorant+Garamond:wght@500&display=swap">
<style>
  :root {
    --backdrop: #e9e6e1;
    --card-dark: #0b0b0b;
    --card-light: #ffffff;
    --brand-blue: #2f6fa8;
    --brand-green: #5a9a3a;
    --ink: #2b2b2b;
    --ink-soft: #555555;
    --ink-light: #e8e8e8;
    --rule: #9a9a9a;
    --box: #8a8a8a;
  }
  * { box-sizing: border-box; margin: 0; padding: 0; }
  html, body { width: 1200px; height: 778px; overflow: hidden; }
  body {
    background: var(--backdrop);
    font-family: "Open Sans", Arial, sans-serif;
    position: relative;
  }
  .card {
    position: absolute;
    box-shadow: 0 3px 10px rgba(0,0,0,.25);
  }
  .card--front { width: 552px; height: 317px; top: 43px; }
  .card--dark { left: 36px; background: var(--card-dark); color: var(--ink-light); }
  .card--light { left: 624px; background: var(--card-light); color: var(--ink); }
  .card--appointment { left: 336px; top: 408px; width: 533px; height: 341px; background: var(--card-light); color: var(--ink); }

  .brand {
    position: absolute;
    display: flex; align-items: center; gap: 10px;
  }
  .brand__dot { width: 22px; height: 22px; border-radius: 50%; background: var(--brand-green); flex: none; }
  .brand__name {
    font-weight: 700; color: var(--brand-blue);
    line-height: 1.05; text-transform: uppercase; letter-spacing: 1px;
  }
  .brand__sub { display: block; }
  .card--front .brand { left: 36px; top: 66px; }
  .card--front .brand__name { font-size: 44px; }
  .card--front .brand__sub { font-size: 17px; letter-spacing: 2.4px; }

  .contacts { position: absolute; left: 36px; top: 196px; list-style: none; font-size: 13px; line-height: 20px; }
  .contacts li { display: flex; align-items: center; gap: 8px; }
  .contacts svg { width: 11px; height: 11px; fill: currentColor; }
  .address { position: absolute; left: 36px; top: 282px; font-size: 13px; }
  .person { position: absolute; right: 30px; top: 196px; text-align: right; }
  .person__name { font-size: 15px; font-weight: 700; }
  .person__title { font-size: 12px; color: var(--ink-soft); }
  .card--dark .person__title { color: #c9c9c9; }

  .card--appointment .brand { right: 30px; top: 20px; }
  .card--appointment .brand__name { font-size: 30px; }
  .card--appointment .brand__sub { font-size: 12px; letter-spacing: 1.6px; }
  .appt__heading {
    position: absolute; left: 30px; top: 78px;
    font-family: "Cormorant Garamond", Georgia, serif; font-weight: 500;
    font-size: 22px; letter-spacing: 1px; color: var(--brand-green);
  }
  .appt__row { position: absolute; left: 30px; display: flex; align-items: center; font-size: 14px; gap: 8px; }
  .appt__line { border-bottom: 1px dotted var(--rule); height: 14px; }
  .appt__box { width: 78px; height: 22px; border: 1px solid var(--box); }
  .appt__day { font-weight: 700; font-size: 14px; }
  .appt__daybox { width: 30px; height: 22px; border: 1px solid var(--box); margin-right: 6px; }
  .appt__note { position: absolute; left: 30px; top: 268px; font-size: 13px; font-style: italic; color: var(--ink-soft); }
</style>
</head>
<body>

<section class="card card--front card--dark">
  <div class="brand">
    <span class="brand__dot"></span>
    <span class="brand__name">Valtor<span class="brand__sub">Chiropractic Clinic</span></span>
  </div>
  <ul class="contacts">
    <li><svg viewBox="0 0 12 12"><path d="M2 1h3l1 3-1.5 1a7 7 0 0 0 2.5 2.5L8 6l3 1v3c0 .6-.4 1-1 1A9 9 0 0 1 1 2c0-.6.4-1 1-1z"/></svg>614 555 0142</li>
    <li><svg viewBox="0 0 12 12"><path d="M3 1h6v3H3zM1 5h10v5H9V8H3v2H1zM3 9h6v2H3z"/></svg>614 555 0178</li>
    <li><svg viewBox="0 0 12 12"><path d="M1 2h10v8H1zm1 1v.5l4 3 4-3V3z"/></svg>kpm@valtorchiro.example</li>
    <li><svg viewBox="0 0 12 12"><circle cx="6" cy="6" r="5"/></svg>www.valtorchiro.example</li>
  </ul>
  <p class="address">28615 Birchmont Lakeview, OH 44990</p>
  <div class="person">
    <p class="person__name">Martin Valtor D.C. D.A.B.C.O.</p>
    <p class="person__title">Chiroptactic Orthopedist</p>
  </div>
</section>

<section class="card card--front card--light">
  <div class="brand">
    <span class="brand__dot"></span>
    <span class="brand__name">Valtor<span class="brand__sub">Chiropractic Clinic</span></span>
  </div>
  <ul class="contacts">
    <li><svg viewBox="0 0 12 12"><path d="M2 1h3l1 3-1.5 1a7 7 0 0 0 2.5 2.5L8 6l3 1v3c0 .6-.4 1-1 1A9 9 0 0 1 1 2c0-.6.4-1 1-1z"/></svg>614 555 0142</li>
    <li><svg viewBox="0 0 12 12"><path d="M3 1h6v3H3zM1 5h10v5H9V8H3v2H1zM3 9h6v2H3z"/></svg>614 555 0178</li>
    <li><svg viewBox="0 0 12 12"><path d="M1 2h10v8H1zm1 1v.5l4 3 4-3V3z"/></svg>kpm@valtorchiro.example</li>
    <li><svg viewBox="0 0 12 12"><circle cx="6" cy="6" r="5"/></svg>www.valtorchiro.example</li>
  </ul>
  <p class="address">28615 Birchmont Lakeview, OH 44990</p>
  <div class="person">
    <p class="person__name">Martin Valtor D.C. D.A.B.C.O.</p>
    <p class="person__title">Chiroptactic Orthopedist</p>
  </div>
</section>

<section class="card card--appointment">
  <div class="brand">
    <span class="brand__dot"></span>
    <span class="brand__name">Valtor<span class="brand__sub">Chiropractic Clinic</span></span>
  </div>
  <h2 class="appt__heading">YOUR APPOINTMENT</h2>
  <div class="appt__row" style="top:116px">Name :<span class="appt__line" style="width:200px"></span></div>
  <div class="appt__row" style="top:154px">Date :<span class="appt__line" style="width:160px"></span>Time :<span class="appt__line" style="width:100px"></span>am / pm</div>
  <div class="appt__row" style="top:190px">Next Appointment<span class="appt__box"></span><span class="appt__box"></span></div>
  <div class="appt__row" style="top:228px;gap:4px">
    <span class="appt__day">MON</span><span class="appt__daybox"></span>
    <span class="appt__day">TUE</span><span class="appt__daybox"></span>
    <span class="appt__day">WED</span><span class="appt__daybox"></span>
    <span class="appt__day">THU</span><span class="appt__daybox"></span>
    <span class="appt__day">FRI</span><span class="appt__daybox"></span>
    <span class="appt__day">SAT</span><span class="appt__daybox"></span>
  </div>
  <p class="appt__note">We appreciate a 24 hr. notice for cancellations</p>
</section>

</body>
</html>
```